Brandlark CEO needs a Crowdsourced Graphic for a Gizmoreel Article

I need a simple graphic / banner for a blog post that's going to be posted on Gizmoreel (www.gizmoreel.example) - the biggest tech blog in the world.

The article will be written by Omar Feltz (Brandlark's CEO) and the title will be "The Quiet Harbor Surge Unveiled". The article is about the tens of thousands of people using crowdsourcing websites (like Brandlark.example, Qtaskly.example and Wervo.example) in China, India, the Philippines, Australia and other countries in the Asia Pacific region.

We'd really like to get this ASAP - so early submissions encouraged. We will try and get the winning designer linked to from the article.
Updates

Thanks to everyone that submitted!  Some great designs and hard to choose! :)

Target Market(s)

Tech saavy readers, English speakers

Industry/Entity Type

Tech

Requirements
Must have
• The graphic SHOULD:
1) Have the text "The quiet harbor surge unveiled" with some nice design and fonts (consider grey subtle pattern background and white drop shadow on fonts) - see attached examples
2) Have an Asian theme
3) Have the dimensions 640px wide by 240px wide
Nice to have
• The graphic COULD:
1) Have references to some or all of the countries mentioned above or use Asian characters as part of the background / motif (maybe the word "crowd" or "crowd sourcing" in different languages). In Chinese, the word for crowdsourcing is "witkey" (and there are corresponding Chinese characters: ??)
2) Emphasize the word "Asia" (using color and larger/different font)
3) Use a chart showing exponential (i.e. fast) growth - like the attached
4) Have a second line of text "7 Odd Facts Hiding Behind the Quiet Harbor Surge"

```html
<!DOCTYPE html>
<html lang="en">
<head>
<meta charset="utf-8">
<title>The Quiet Harbor Surge Unveiled</title>
<link rel="stylesheet" href="https://fonts.googleapis.com/css2?family=Almendra+Display&family=Uncial+Antiqua&family=Questrial&family=Noto+Sans+Devanagari:wght@400;700&family=Noto+Sans+SC:wght@400;700&display=swap">
<style>
  :root {
    --bg-light: #eeeeee;
    --bg-mid: #dedede;
    --motif-grey: #c9c9c9;
    --motif-dark: #b9b9b9;
    --title-red: #b3121c;
    --chart-red: #c8101a;
    --chart-fill: #d3d5dd;
    --box-border: #6a6a6a;
    --text-dark: #2e2e2e;
    --white: #ffffff;
  }
  * { margin: 0; padding: 0; box-sizing: border-box; }
  html, body { width: 1200px; height: 450px; overflow: hidden; background: var(--bg-light); }
  .banner {
    position: relative;
    width: 1200px;
    height: 450px;
    overflow: hidden;
    background:
      radial-gradient(ellipse at 35% 40%, var(--bg-light) 0%, var(--bg-mid) 100%);
  }
  .motif-word {
    position: absolute;
    color: var(--motif-grey);
    white-space: nowrap;
    line-height: 1;
  }
  .motif-word.hindi { font-family: "Noto Sans Devanagari", sans-serif; font-weight: 700; }
  .motif-word.chinese { font-family: "Noto Sans SC", sans-serif; font-weight: 400; }
  .motif-word.tagalog { font-family: "Questrial", sans-serif; font-weight: 700; }
  .hands-art {
    position: absolute;
    left: 620px;
    top: 0;
    width: 580px;
    height: 380px;
    background: radial-gradient(ellipse at 55% 55%, rgba(150,150,150,0.45) 0%, rgba(170,170,170,0.25) 45%, rgba(200,200,200,0) 75%);
  }
  .growth-chart { position: absolute; left: 0; top: 0; width: 1200px; height: 450px; }
  .ornament {
    position: absolute;
    left: 9px;
    top: 34px;
    width: 188px;
    height: 188px;
    border-radius: 50%;
    background: radial-gradient(circle, #f4f4f4 0%, #9a9a9a 35%, #e8e8e8 55%, #6e6e6e 80%, #dcdcdc 100%);
  }
  .title {
    position: absolute;
    left: 238px;
    top: 28px;
    color: var(--title-red);
    text-shadow: 2px 2px 0 var(--white);
  }
  .title-lead {
    display: block;
    font-family: "Almendra Display", serif;
    font-size: 112px;
    line-height: 1;
  }
  .title-rest {
    display: block;
    margin-top: 4px;
    font-family: "Uncial Antiqua", serif;
    font-size: 54px;
    line-height: 1;
    letter-spacing: 1px;
  }
  .subtitle {
    position: absolute;
    left: 219px;
    top: 244px;
    display: flex;
    align-items: center;
    gap: 18px;
    font-family: "Questrial", sans-serif;
    color: var(--text-dark);
  }
  .subtitle-count {
    width: 44px;
    height: 48px;
    border: 2px solid var(--box-border);
    border-radius: 6px;
    background: var(--white);
    font-size: 42px;
    line-height: 44px;
    text-align: center;
  }
  .subtitle-text {
    height: 42px;
    padding: 0 16px;
    border: 2px solid var(--box-border);
    border-radius: 8px;
    background: var(--white);
    font-size: 29px;
    line-height: 38px;
    white-space: nowrap;
  }
</style>
</head>
<body>
<div class="banner">
  <span class="motif-word hindi" style="left:60px;top:12px;font-size:44px;">भीड</span>
  <span class="motif-word chinese" style="left:175px;top:4px;font-size:50px;">眾包</span>
  <span class="motif-word tagalog" style="left:375px;top:6px;font-size:38px;">karamihan ng tao</span>
  <span class="motif-word hindi" style="left:690px;top:18px;font-size:48px;">भीड</span>
  <span class="motif-word chinese" style="left:800px;top:16px;font-size:48px;">眾包</span>
  <span class="motif-word chinese" style="left:1045px;top:0;font-size:54px;">眾包</span>
  <span class="motif-word chinese" style="left:590px;top:78px;font-size:36px;">眾包</span>
  <span class="motif-word hindi" style="left:690px;top:110px;font-size:32px;">भीड</span>
  <span class="motif-word chinese" style="left:860px;top:88px;font-size:40px;">眾包</span>

  <div class="hands-art" role="img" aria-label="Silhouettes of many raised hands, fading grey"></div>

  <svg class="growth-chart" viewBox="0 0 1200 450" aria-hidden="true">
    <path d="M403 450 L491 411 L666 371 L919 349 L1149 279 L1200 200 L1200 450 Z" fill="var(--chart-fill)"/>
    <polyline points="403,450 491,411 666,371 919,349 1149,279 1200,200" fill="none" stroke="var(--chart-red)" stroke-width="6" stroke-linejoin="round"/>
    <g fill="var(--chart-red)" stroke="var(--white)" stroke-width="3">
      <circle cx="491" cy="411" r="15"/>
      <circle cx="666" cy="371" r="15"/>
      <circle cx="919" cy="349" r="15"/>
      <circle cx="1149" cy="279" r="15"/>
    </g>
  </svg>

  <div class="ornament" role="img" aria-label="Round black and white lotus mandala ornament"></div>

  <h1 class="title">
    <span class="title-lead">The quiet</span>
    <span class="title-rest">harbor surge unveiled</span>
  </h1>

  <div class="subtitle">
    <span class="subtitle-count">7</span>
    <span class="subtitle-text">Odd Facts Hiding Behind the Quiet Harbor Surge</span>
  </div>
</div>
</body>
</html>
```